Moder Business Card Design for Renewables Business

Need a business card design for my business. We collect & repurpose spent coffee ground from cafes. The cards will be made from recycled paper. Needs to fit our corporate colour scheme of white, green & brown (see logo for colour codes). Eco friendly, modern, intresting & eye catching.
This card needs to convey the message of the business and fit into its mantra of eco-friendly, sustainable etc.

Target Market(s)

Cafe Owners, Coffee Drinkers, Recycling Companies, Farmers

Industry/Entity Type

Recycling

Contact Information for Business Card

Name; Peter Halloran
Phone; 0412 386 527
e-mail; info@lumatrove.com.au
website; www.lumatrove.com.au

Font styles to use
Sans Serif
Script

Colors

Designer to choose colors to be used in the design.

Requirements
Must have
• FRONT;
• Logo, Name (Peter Halloran), phone number, e-mail address, website
• BACK;
• On the back in cursive text; 'GOOD GROUNDS FOR A GREENER FUTURE'
• Small facebook & Instagram logos with text 'Lumatrove'
Should not have
• messy design

```html
<!DOCTYPE html>
<html lang="en">
<head>
<meta charset="utf-8">
<title>Lumatrove Business Card</title>
<link href="https://fonts.googleapis.com/css2?family=Open+Sans:wght@400;600&display=swap" rel="stylesheet">
<style>
  :root {
    --page-bg: #3a332f;
    --card-bg: #141414;
    --green: #7bb83a;
    --brown: #8a4a1c;
    --orange: #c2662a;
    --text-light: #d8d8d8;
    --silver: #c9c9c9;
    --rule: #5a5a5a;
    --social: #dfe6ee;
  }
  * { box-sizing: border-box; margin: 0; padding: 0; }
  html, body {
    width: 1200px; height: 844px; overflow: hidden;
    background: var(--page-bg);
    font-family: "Open Sans", Arial, sans-serif;
  }
  .stage {
    width: 1200px; height: 844px;
    display: flex; align-items: center; justify-content: center; gap: 40px;
  }
  .card {
    width: 540px; height: 310px;
    background: var(--card-bg);
    position: relative;
    box-shadow: 0 10px 30px rgba(0,0,0,.45);
  }

  /* Front */
  .brand {
    position: absolute; left: 40px; top: 58px; width: 170px;
    display: flex; flex-direction: column; align-items: center;
  }
  .brand-circle {
    width: 112px; height: 112px; border-radius: 50%;
    border: 6px solid var(--brown);
  }
  .brand-name {
    margin-top: 12px;
    color: var(--green);
    font-size: 22px; font-weight: 600; letter-spacing: .5px;
    white-space: nowrap;
  }
  .divider {
    position: absolute; left: 232px; top: 36px;
    width: 1px; height: 150px; background: var(--rule);
  }
  .contact {
    position: absolute; left: 262px; top: 44px;
  }
  .person {
    font-size: 19px; font-weight: 600; letter-spacing: .5px; margin-bottom: 26px;
    white-space: nowrap;
  }
  .person .first { color: var(--orange); }
  .person .last { color: var(--green); }
  .contact-list { list-style: none; }
  .contact-list li {
    display: flex; align-items: center; gap: 9px;
    color: var(--text-light); font-size: 15px; line-height: 22px;
    white-space: nowrap;
  }
  .contact-list svg { width: 12px; height: 12px; fill: var(--orange); flex: none; }
  .tagline {
    position: absolute; left: 0; right: 0; bottom: 34px;
    text-align: center;
    color: var(--text-light); font-size: 17px; letter-spacing: .3px;
    white-space: nowrap;
  }

  /* Back */
  .back {
    display: flex; flex-direction: column; align-items: center;
  }
  .back-mark {
    margin-top: 34px;
    width: 116px; height: 116px; border-radius: 50%;
    border: 5px solid var(--silver);
    display: flex; align-items: center; justify-content: center;
  }
  .back-mark span {
    color: var(--silver); font-size: 14px; font-weight: 600; letter-spacing: 1px;
  }
  .rule { width: 240px; height: 1px; background: var(--rule); }
  .rule.upper { margin-top: 18px; }
  .social { display: flex; gap: 6px; margin-top: 8px; }
  .social-dot { width: 22px; height: 22px; border-radius: 50%; background: var(--social); }
  .social-handle { color: var(--text-light); font-size: 13px; margin: 4px 0 10px; }
</style>
</head>
<body>
<main class="stage">
  <section class="card front">
    <div class="brand">
      <div class="brand-circle"></div>
      <div class="brand-name">LUMATROVE</div>
    </div>
    <div class="divider"></div>
    <div class="contact">
      <div class="person"><span class="first">PETER</span> <span class="last">HALLORAN</span></div>
      <ul class="contact-list">
        <li><svg viewBox="0 0 12 12"><path d="M2 1h3l1 3-1.5 1a6 6 0 0 0 2.5 2.5L8 6l3 1v3c0 .6-.4 1-1 1A9 9 0 0 1 1 2c0-.6.4-1 1-1z"/></svg>0412 386 527</li>
        <li><svg viewBox="0 0 12 12"><path d="M1 2h10v1L6 6.5 1 3zM1 4.2l5 3.5 5-3.5V10H1z"/></svg>info@lumatrove.com.au</li>
        <li><svg viewBox="0 0 12 12"><circle cx="6" cy="6" r="5"/></svg>www.lumatrove.com.au</li>
      </ul>
    </div>
    <p class="tagline">GOOD GROUNDS FOR A GREENER FUTURE</p>
  </section>

  <section class="card back">
    <div class="back-mark"><span>LUMATROVE</span></div>
    <div class="rule upper"></div>
    <div class="social">
      <div class="social-dot"></div>
      <div class="social-dot"></div>
    </div>
    <div class="social-handle">Lumatrove</div>
    <div class="rule"></div>
  </section>
</main>
</body>
</html>
```